Organic Food Producer Needs Business Card

We need an attractive business card that is both trendy and professional. We are a FQRB, Vetra Clear Certified organic producer of coconut oil, coconut flour and additional cacao products. We produce some of the world's purest coconut oil and coconut oil derived products in the world.
We take pride in the purity of our products and the transparency with which we create our products. Use of FQRB Organic and Vetra Clear logos is acceptable and preferred. The final design would reflect our values for purity and the natural state of our products.
The business card should include: job title, email address, phone number and facebook, twitter, instagram tag.
Don't be afraid to get creative! I have attached some of our packaging design in JPG format as well as our logo. The jpgs dont display the colors correctly in chrome but they will display correctly if you DL and open them in photoshop.
Target Market(s)
Cards likely to be used in organic food industry events for people such as buyers, trade show reps, etc... but also store owners and people casually interested in.
The company's target market :
Primary:
Women - 22-65. Women typically hold the household budget and make the purchasing decisions at the supermarket. They are interested in quality healthy and beauty products at a good value. Organic, fair trade, artisanally made are all important attributes of brands they purchase. They try to maintain a healthy lifestyle through proper eating, exercise and work/life balance.
Secondary:
Men - 44% of American adults are single so it is important to note that men will also be a key target audience. And they too are concerned and passionate about organic, fair trade, artisanally made, good value and living a healthy lifestyle.
Tertiary:
Health & Wellness Professionals (Nutritionists, Doctors, etc) Coconut is highly nutritional and more and more, it is being recommended as part of a healthy diet by professionals. We should keep this audience in mind as well, particularly when we build a website with useful resources such as the company’s high standards, the health benefits of coconut, nutrition info and recipes.
Industry/Entity Type
Business
Requirements
Must have
- Pretty open minded about creativity and variety, I do like the color palettes in the labeling files provided... but it is not a deal breaker to vary from this.
Should be visually impacting.
Nice to have
- Would like to have some creative use of raised lettering or detail.
Should not have
- Although the company is based in the caribbean, we are not looking for an overly ethnic caribbean feel.
You should open the attached files in photoshop, as they seem to distort the color in a web browser.

```html
<!DOCTYPE html>
<html lang="en">
<head>
<meta charset="utf-8">
<title>clearleaf — business card</title>
<link rel="stylesheet" href="https://fonts.googleapis.com/css2?family=Source+Sans+3:wght@400;600&display=swap">
<style>
  :root {
    --cocoa: #3c2210;
    --lagoon: #0a8aa6;
    --shallows: #a3dbe6;
    --sand: #fde4b6;
    --leaf: #4f8a3c;
    --page: #ffffff;
  }
  * { margin: 0; padding: 0; box-sizing: border-box; }
  html, body {
    width: 1200px; height: 1066px; overflow: hidden;
    background: var(--page);
    font-family: "Source Sans 3", "Myriad Pro", sans-serif;
  }
  .stage { position: relative; width: 1200px; height: 1066px; }

  .card {
    position: absolute; width: 736px; height: 480px; overflow: hidden;
  }

  /* card back: brand side */
  .card--brand { left: 67px; top: 73px; background: var(--cocoa); }
  .brand-disc {
    position: absolute; left: 483px; top: -14px;
    width: 492px; height: 492px; border-radius: 50%;
    background: var(--lagoon);
  }
  .wordmark {
    position: absolute; left: 86px; top: 200px;
    display: flex; align-items: center; gap: 16px;
  }
  .wordmark__dot {
    width: 34px; height: 34px; border-radius: 50%; background: var(--shallows);
  }
  .wordmark__name {
    font-size: 58px; font-weight: 400; line-height: 1; color: var(--shallows);
    letter-spacing: 1px;
  }
  .tagline {
    position: absolute; left: 136px; top: 272px;
    font-size: 18px; color: var(--sand); letter-spacing: 1.2px;
  }

  /* card front: contact side */
  .card--contact { left: 366px; top: 483px; background: var(--sand); }
  .band {
    position: absolute; left: 0; width: 100%;
  }
  .band--name { top: 153px; height: 73px; background: var(--cocoa); }
  .band--title { top: 226px; height: 31px; background: var(--lagoon); }
  .contact-disc {
    position: absolute; left: -242px; top: -5px;
    width: 492px; height: 492px; border-radius: 50%;
    background: var(--lagoon);
  }
  .cert { position: absolute; }
  .cert--square { left: 556px; top: 39px; width: 80px; height: 49px; background: var(--leaf); }
  .cert--round { left: 654px; top: 37px; width: 52px; height: 52px; border-radius: 50%; background: var(--page); border: 4px solid var(--leaf); }

  .person-name {
    position: absolute; left: 360px; top: 168px;
    font-size: 31px; color: var(--sand); line-height: 1;
  }
  .person-title {
    position: absolute; left: 360px; top: 229px;
    font-size: 19px; color: var(--sand); line-height: 1.2;
  }
  .contact {
    position: absolute; left: 360px; top: 290px;
    list-style: none; font-size: 17px; line-height: 23.5px; color: var(--cocoa);
  }
  .contact__phone {
    font-size: 36px; line-height: 1; color: var(--lagoon); margin-bottom: 6px;
  }
  .contact__label { color: var(--lagoon); }
</style>
</head>
<body>
<main class="stage">

  <section class="card card--brand" aria-label="Card back">
    <div class="brand-disc" role="img" aria-label="Large brand emblem area"></div>
    <div class="wordmark">
      <span class="wordmark__dot"></span>
      <span class="wordmark__name">clearleaf</span>
    </div>
    <p class="tagline">handcrafted in the caribbean</p>
  </section>

  <section class="card card--contact" aria-label="Card front">
    <div class="band band--name"></div>
    <div class="band band--title"></div>
    <div class="contact-disc" role="img" aria-label="Large brand emblem area"></div>

    <div class="cert cert--square" role="img" aria-label="Vetra Clear verified badge"></div>
    <div class="cert cert--round" role="img" aria-label="FQRB organic badge"></div>

    <h1 class="person-name" style="font-weight:400">mara quinlan</h1>
    <p class="person-title">managing director</p>

    <ul class="contact">
      <li class="contact__phone">5550 123 456</li>
      <li>mara@clearleafco.com</li>
      <li><span class="contact__label">facebook.com/</span>clearleafco</li>
      <li><span class="contact__label">twitter:</span> @clearleafco</li>
      <li><span class="contact__label">instagram:</span> #clearleafco</li>
    </ul>
  </section>

</main>
</body>
</html>
```